Bref créative
Limb Nestler
Naturally made in the US
Professional
Rosalind Featherstone
Owner
437 Tamsin Ave - Ste 220-581
rfeatherstone@limbnestler-example.com
Limbnestler-example.com
I'm not sure what the first two boxes refer to. I want our logo to be on the cards in the same colors.

```html
<!DOCTYPE html>
<html lang="en">
<head>
<meta charset="utf-8">
<title>Limb Nestler — Stationery</title>
<link href="https://fonts.googleapis.com/css2?family=Montserrat:wght@400;500;600;700&display=swap" rel="stylesheet">
<style>
:root{
  --maroon:#6b2222;
  --maroon-dark:#571a1a;
  --blue:#1c9ad6;
  --paper:#ffffff;
  --ink:#555555;
  --faint:#ece6e4;
  --backdrop:#eee4d4;
}
*{margin:0;padding:0;box-sizing:border-box}
html,body{width:1200px;height:610px;overflow:hidden}
body{background:var(--backdrop);font-family:"Montserrat",sans-serif;color:var(--ink);position:relative}

.brand{display:flex;align-items:center;gap:6px;color:var(--maroon);font-weight:600;white-space:nowrap}
.brand-dot{display:inline-block;border-radius:50%;background:var(--maroon)}

.contact{list-style:none;font-size:5px;line-height:8px;color:var(--ink)}
.contact li{display:flex;align-items:center;gap:3px}
.contact svg{width:5px;height:5px;flex:none}

/* business card */
.business-card{position:absolute;left:48px;top:206px;width:192px;height:154px;background:var(--paper);border-radius:10px;box-shadow:0 2px 5px rgba(0,0,0,.18);overflow:hidden}
.business-card .edge-maroon{position:absolute;left:0;top:0;bottom:0;width:4px;background:var(--maroon)}
.business-card .edge-blue{position:absolute;left:4px;top:0;bottom:0;width:2px;background:var(--blue)}
.business-card .brand{position:absolute;left:14px;top:34px;font-size:10px}
.business-card .brand-dot{width:10px;height:10px}
.business-card .holder{position:absolute;left:100px;top:26px}
.holder-name{font-size:7px;font-weight:700;color:#333}
.holder-role{font-size:5px;color:var(--maroon);margin-bottom:7px}

/* letterhead */
.letterhead{position:absolute;left:240px;top:36px;width:290px;height:540px;background:var(--paper);box-shadow:0 2px 6px rgba(0,0,0,.18);overflow:hidden}
.letterhead .brand{position:absolute;left:20px;top:26px;font-size:12px}
.letterhead .brand-dot{width:12px;height:12px}
.letterhead .contact{position:absolute;left:208px;top:14px}
.letterhead .watermark{position:absolute;left:-10px;top:200px;width:220px;height:220px;border-radius:50%;background:var(--faint)}
.letterhead .rule-side{position:absolute;left:0;top:400px;width:6px;height:140px;border-left:4px solid var(--maroon);border-right:2px solid var(--blue)}
.letterhead .rule-mid{position:absolute;left:270px;top:276px;width:6px;height:168px;border-left:4px solid var(--maroon);border-right:2px solid var(--blue)}

/* standalone mark */
.brand-showcase{position:absolute;left:800px;top:62px;font-size:26px}
.brand-showcase .brand-dot{width:24px;height:24px}

/* envelopes */
.envelope{position:absolute;background:var(--paper);box-shadow:0 2px 6px rgba(0,0,0,.2);overflow:hidden}
.envelope-back{left:560px;top:230px;width:500px;height:170px}
.envelope-back svg{position:absolute;inset:0}
.envelope-back .brand{position:absolute;left:330px;top:26px;font-size:14px}
.envelope-back .brand-dot{width:13px;height:13px}
.envelope-flap{left:600px;top:330px;width:520px;height:120px;background:transparent;box-shadow:none}
.envelope-flap svg{position:absolute;inset:0}
.envelope-flap .brand{position:absolute;left:205px;top:30px;font-size:16px;color:#fff}
.envelope-flap .brand-dot{width:14px;height:14px;background:#fff}
.envelope-front{left:620px;top:410px;width:520px;height:180px}
.envelope-front .brand{position:absolute;left:40px;top:22px;font-size:13px}
.envelope-front .brand-dot{width:12px;height:12px}
.envelope-front .contact{position:absolute;left:36px;top:116px}
.envelope-front .watermark{position:absolute;left:390px;top:60px;width:150px;height:150px;border-radius:50%;background:var(--faint)}
</style>
</head>
<body>

<svg width="0" height="0" style="position:absolute">
  <defs>
    <symbol id="icon-pin" viewBox="0 0 10 10"><path d="M5 0a3.5 3.5 0 0 1 3.5 3.5C8.5 6 5 10 5 10S1.5 6 1.5 3.5A3.5 3.5 0 0 1 5 0z" fill="#777"/></symbol>
    <symbol id="icon-phone" viewBox="0 0 10 10"><path d="M2 0h2l1 3-1.5 1a6 6 0 0 0 2.5 2.5L7 5l3 1v2a2 2 0 0 1-2 2A8 8 0 0 1 0 2a2 2 0 0 1 2-2z" fill="#777"/></symbol>
    <symbol id="icon-mail" viewBox="0 0 10 10"><rect x="0" y="2" width="10" height="6" fill="#777"/></symbol>
    <symbol id="icon-web" viewBox="0 0 10 10"><circle cx="5" cy="5" r="4.5" fill="#777"/></symbol>
  </defs>
</svg>

<section class="business-card">
  <span class="edge-maroon"></span><span class="edge-blue"></span>
  <div class="brand"><span class="brand-dot"></span>Limb Nestler</div>
  <div class="holder">
    <p class="holder-name">Rosalind Featherstone</p>
    <p class="holder-role">Owner</p>
    <ul class="contact">
      <li><svg><use href="#icon-pin"/></svg>437 Tamsin Ave - Ste 220-581</li>
      <li><svg><use href="#icon-phone"/></svg>555-014-2290</li>
      <li><svg><use href="#icon-phone"/></svg>555-017-3384</li>
      <li><svg><use href="#icon-mail"/></svg>rfeatherstone@limbnestler-example.com</li>
      <li><svg><use href="#icon-web"/></svg>Limbnestler-example.com</li>
    </ul>
  </div>
</section>

<section class="letterhead">
  <span class="watermark"></span>
  <div class="brand"><span class="brand-dot"></span>Limb Nestler</div>
  <ul class="contact">
    <li>437 Tamsin Ave - Ste 220-581</li>
    <li><svg><use href="#icon-phone"/></svg>555-014-2290</li>
    <li><svg><use href="#icon-phone"/></svg>555-017-3384</li>
    <li><svg><use href="#icon-mail"/></svg>rfeatherstone@limbnestler-example.com</li>
    <li><svg><use href="#icon-web"/></svg>Limbnestler-example.com</li>
  </ul>
  <span class="rule-side"></span>
  <span class="rule-mid"></span>
</section>

<div class="brand brand-showcase"><span class="brand-dot"></span>Limb Nestler</div>

<section class="envelope envelope-back">
  <svg viewBox="0 0 500 170" preserveAspectRatio="none">
    <polygon points="0,0 500,0 500,14 250,90 0,14" fill="var(--blue)"/>
    <polygon points="0,14 250,90 500,14 500,20 250,96 0,20" fill="#ffffff"/>
  </svg>
  <div class="brand"><span class="brand-dot"></span>Limb Nestler</div>
</section>

<section class="envelope envelope-front">
  <span class="watermark"></span>
  <div class="brand"><span class="brand-dot"></span>Limb Nestler</div>
  <ul class="contact">
    <li><svg><use href="#icon-pin"/></svg>437 Tamsin Ave - Ste 220-581</li>
    <li><svg><use href="#icon-phone"/></svg>555-014-2290</li>
    <li><svg><use href="#icon-phone"/></svg>555-017-3384</li>
    <li><svg><use href="#icon-mail"/></svg>rfeatherstone@limbnestler-example.com</li>
    <li><svg><use href="#icon-web"/></svg>Limbnestler-example.com</li>
  </ul>
</section>

<section class="envelope envelope-flap">
  <svg viewBox="0 0 520 120" preserveAspectRatio="none">
    <polygon points="0,0 520,0 520,40 260,120 0,40" fill="var(--maroon)"/>
    <polygon points="0,0 520,0 520,6 0,6" fill="var(--maroon-dark)"/>
  </svg>
  <div class="brand"><span class="brand-dot"></span>Limb Nestler</div>
</section>

</body>
</html>
```